Banner for home page on event planning site

We are revamping the home page www.coralbellecelebrations.com and would like to add a banner to the center of it to guide potential clients to one of 3 areas of the site:

Weddings, Corporate Events, Parties and More

I'm uploading an attachment that shows where the banner will be placed. It needs to have those 3 distinct sections, and match the existing colors/branding of the site. The fonts used for the logo are Lucida Bright and Callie Hand. Both are available for free.

Please use lorem ipsum under each section, I'll fill that in later. It should just be highly designed, beautiful, and easy to understand that clicking these will take you to the different areas of the site.
Updates

Hi designers,
Here are some problems we are having with the designs that have been submitted.
1) 3 stock images as squares... when you do this and then put it into the existing website, it gets lost among the other boxes. We need this to be where the eye goes immediately when you land on the site.
2) Not enough of a frame or white space... we think you need some white space to make this stand out as different from the surrounding area.
3) No clearly defined areas. It needs to be easy for people to figure out... Weddings, click here. Parties, click here. Corporate events, click here.

Industry/Entity Type

Event Planning

Requirements
Should not have
• Nothing with orchids, her competitor uses them and they are common in the event planning industry. We want to stay away from them.

Files

```html
<!DOCTYPE html>
<html lang="en">
<head>
<meta charset="utf-8">
<title>Home Page Banner</title>
<link rel="stylesheet" href="https://fonts.googleapis.com/css2?family=Allura&display=swap">
<style>
  :root {
    --canvas: #ffffff;
    --frame-grey: #737376;
    --frame-grey-light: #7d7d80;
    --rule-grey: #c9c9c9;
    --pink: #b84a8f;
    --pink-deep: #8c2f6b;
    --gold-dark: #7a4a15;
    --gold-mid: #b8862e;
    --gold-light: #efe0a0;
    --gold-shine: #fffbe8;
    --type: #ffffff;
  }
  * { box-sizing: border-box; margin: 0; padding: 0; }
  html, body {
    width: 1200px; height: 616px; overflow: hidden;
    background: var(--canvas);
  }
  .canvas { position: relative; width: 1200px; height: 616px; }

  .banner { position: absolute; left: 0; width: 1200px; }
  .banner--framed {
    top: 0; height: 270px;
    background: linear-gradient(180deg, var(--frame-grey-light), var(--frame-grey));
    box-shadow: 0 6px 6px rgba(0,0,0,0.35);
  }
  .banner--plain {
    top: 348px; height: 268px;
    background: var(--canvas);
    border: 1px solid var(--rule-grey);
  }

  .card {
    position: absolute;
    width: 337px; height: 214px;
    overflow: hidden;
    display: block;
    text-decoration: none;
    background: var(--pink);
  }
  .banner--framed .card { top: 27px; }
  .banner--plain .card { top: 27px; box-shadow: 0 0 3px rgba(0,0,0,0.25); }
  .card--weddings { left: 39px; }
  .card--corporate { left: 434px; }
  .card--parties { left: 828px; }
  .banner--framed .card::after {
    content: ""; position: absolute; inset: 0;
    box-shadow: inset 4px 4px 8px rgba(0,0,0,0.45);
    pointer-events: none;
  }

  .card__art { position: absolute; inset: 0; width: 100%; height: 100%; }

  .card__label {
    position: absolute; left: 0; right: 0;
    font-family: "Allura", cursive;
    font-weight: 400;
    color: var(--type);
    text-align: center;
    font-size: 66px;
    line-height: 58px;
    white-space: nowrap;
    text-shadow: 3px 5px 5px rgba(60,10,40,0.55);
  }
  .card--weddings .card__label { top: 114px; left: -12px; }
  .card--corporate .card__label { top: 96px; left: 8px; }
  .card--parties .card__label { top: 84px; left: 20px; }
</style>
</head>
<body>
<svg width="0" height="0" style="position:absolute" aria-hidden="true">
  <defs>
    <linearGradient id="gold-sweep" x1="0" y1="0" x2="1" y2="0">
      <stop offset="0" stop-color="#6e3f10"/>
      <stop offset="0.3" stop-color="#a8752a"/>
      <stop offset="0.6" stop-color="#e9d48a"/>
      <stop offset="0.78" stop-color="#fffbe8"/>
      <stop offset="0.9" stop-color="#e8d080"/>
      <stop offset="1" stop-color="#b8862e"/>
    </linearGradient>
    <linearGradient id="gold-sweep-rev" x1="1" y1="0" x2="0" y2="0">
      <stop offset="0" stop-color="#6e3f10"/>
      <stop offset="0.3" stop-color="#a8752a"/>
      <stop offset="0.6" stop-color="#e9d48a"/>
      <stop offset="0.78" stop-color="#fffbe8"/>
      <stop offset="0.9" stop-color="#e8d080"/>
      <stop offset="1" stop-color="#b8862e"/>
    </linearGradient>
    <linearGradient id="gold-pale" x1="0" y1="0" x2="0" y2="1">
      <stop offset="0" stop-color="#fffbe8"/>
      <stop offset="0.6" stop-color="#efe0a0"/>
      <stop offset="1" stop-color="#d8b65e"/>
    </linearGradient>
    <linearGradient id="gold-wing" x1="0" y1="0" x2="1" y2="0">
      <stop offset="0" stop-color="#6e3f10"/>
      <stop offset="0.5" stop-color="#b8862e"/>
      <stop offset="1" stop-color="#e4c978"/>
    </linearGradient>
    <linearGradient id="gold-wing-rev" x1="1" y1="0" x2="0" y2="0">
      <stop offset="0" stop-color="#6e3f10"/>
      <stop offset="0.5" stop-color="#b8862e"/>
      <stop offset="1" stop-color="#e4c978"/>
    </linearGradient>

    <symbol id="art-weddings" viewBox="0 0 337 214">
      <rect width="337" height="214" fill="#b84a8f"/>
      <path d="M0 96 C90 70 200 50 337 54 L337 64 C200 62 100 82 0 106 Z" fill="#8c2f6b"/>
      <path d="M0 0 H337 V54 C200 50 90 70 0 96 Z" fill="url(#gold-sweep)"/>
      <path d="M0 0 H337 V10 H0 Z" fill="#6e3f10" opacity="0.55"/>
    </symbol>
    <symbol id="art-corporate" viewBox="0 0 337 214">
      <rect width="337" height="214" fill="#b84a8f"/>
      <path d="M0 44 C70 40 140 70 168 120 C196 70 266 40 337 44 L337 56 C270 54 200 80 168 128 C136 80 66 54 0 56 Z" fill="#8c2f6b"/>
      <path d="M0 0 H337 V44 C266 40 196 70 168 120 C140 70 70 40 0 44 Z" fill="url(#gold-pale)"/>
      <path d="M0 14 C70 12 140 50 168 120 C130 60 60 40 0 44 Z" fill="url(#gold-wing)"/>
      <path d="M337 14 C266 12 196 50 168 120 C206 60 276 40 337 44 Z" fill="url(#gold-wing-rev)"/>
      <path d="M0 0 H337 V8 H0 Z" fill="#6e3f10" opacity="0.5"/>
    </symbol>
    <symbol id="art-parties" viewBox="0 0 337 214">
      <rect width="337" height="214" fill="#b84a8f"/>
      <path d="M0 52 C137 50 247 70 337 92 L337 102 C240 80 137 62 0 62 Z" fill="#8c2f6b"/>
      <path d="M0 0 H337 V92 C247 70 137 50 0 52 Z" fill="url(#gold-sweep-rev)"/>
      <path d="M0 0 H337 V10 H0 Z" fill="#6e3f10" opacity="0.55"/>
    </symbol>
  </defs>
</svg>

<main class="canvas">
  <section class="banner banner--framed" role="img" aria-label="Grey frame with subtle damask pattern">
    <a class="card card--weddings" href="#weddings">
      <svg class="card__art" viewBox="0 0 337 214" aria-hidden="true"><use href="#art-weddings"/></svg>
      <h2 class="card__label">Weddings</h2>
    </a>
    <a class="card card--corporate" href="#corporate-events">
      <svg class="card__art" viewBox="0 0 337 214" aria-hidden="true">
        <use href="#art-corporate"/>
        <rect x="128" y="33" width="81" height="4" rx="2" fill="#c9a24a" role="img" aria-label="Small gold flourish ornament"/>
      </svg>
      <h2 class="card__label">Corporate<br>Events</h2>
    </a>
    <a class="card card--parties" href="#parties">
      <svg class="card__art" viewBox="0 0 337 214" aria-hidden="true"><use href="#art-parties"/></svg>
      <h2 class="card__label">Parties<br>and More</h2>
    </a>
  </section>

  <section class="banner banner--plain">
    <a class="card card--weddings" href="#weddings">
      <svg class="card__art" viewBox="0 0 337 214" aria-hidden="true"><use href="#art-weddings"/></svg>
      <h2 class="card__label">Weddings</h2>
    </a>
    <a class="card card--corporate" href="#corporate-events">
      <svg class="card__art" viewBox="0 0 337 214" aria-hidden="true">
        <use href="#art-corporate"/>
        <rect x="128" y="33" width="81" height="4" rx="2" fill="#c9a24a" role="img" aria-label="Small gold flourish ornament"/>
      </svg>
      <h2 class="card__label">Corporate<br>Events</h2>
    </a>
    <a class="card card--parties" href="#parties">
      <svg class="card__art" viewBox="0 0 337 214" aria-hidden="true"><use href="#art-parties"/></svg>
      <h2 class="card__label">Parties<br>and More</h2>
    </a>
  </section>
</main>
</body>
</html>
```